Social Media Overlay for Ormond Real Estate

We need an social media overlay that can be added to a photo of a house that includes our current logo and a call to action of "Just Listed". This needs to be something that we can use for every new house that we list. Attached is our current logo in both company colors, purple and white. An example of a overlay from Plazeo that we like.

Target Market(s)

Social Media Real Estate Community - Real Estate Agents, Brokers, Buyers & Sellers

Industry/Entity Type

Real Estate

Font styles to use
Sans Serif

Colors
6c459b

Requirements
Must have
• the company colors, purple and white and the company logo
Nice to have
• call to action "Just Listed"
• some layered, texture, or 3-D effect
Should not have
• Should be clean and simple; nothing too busy

```html
<!DOCTYPE html>
<html lang="en">
<head>
<meta charset="utf-8">
<title>Ormond Real Estate – Just Listed Overlay</title>
<link rel="stylesheet" href="https://fonts.googleapis.com/css2?family=Oswald:wght@700&family=Poppins:wght@500&display=swap">
<style>
  :root {
    --purple: #6c459b;
    --purple-deep: #4a2070;
    --purple-glow: #c9a6ea;
    --white: #ffffff;
    --photo-top: #8aa37a;
    --photo-bottom: #5f7a4c;
  }
  * { margin: 0; padding: 0; box-sizing: border-box; }
  html, body { width: 1200px; height: 555px; overflow: hidden; background: var(--white); }
  .overlay { position: relative; width: 1200px; height: 555px; overflow: hidden; }

  .listing-photo {
    position: absolute; inset: 0;
    background: linear-gradient(180deg, var(--photo-top) 0%, var(--photo-bottom) 100%);
  }

  .ribbon { position: absolute; left: 0; top: 48px; width: 394px; height: 73px; }
  .ribbon svg { position: absolute; inset: 0; }
  .ribbon-label {
    position: absolute; left: 78px; top: 50%; transform: translateY(-50%);
    font-family: "Oswald", "Arial Narrow", sans-serif; font-weight: 700;
    font-size: 56px; line-height: 1; color: var(--purple-deep);
    letter-spacing: -1.5px; text-transform: uppercase; white-space: nowrap;
  }

  .brand-wave { position: absolute; left: 0; top: 0; width: 1200px; height: 555px; }

  .brand-name {
    position: absolute; left: 60px; top: 370px;
    font-family: "Poppins", "Helvetica", sans-serif; font-weight: 500;
    color: var(--white); line-height: 1; white-space: nowrap;
  }
  .brand-name .brand-main { display: block; font-size: 86px; letter-spacing: -2px; }
  .brand-name .brand-sub { display: block; font-size: 46px; margin: -2px 0 0 12px; letter-spacing: -0.5px; }
</style>
</head>
<body>
<div class="overlay">
  <div class="listing-photo" role="img" aria-label="Photo of the newly listed house"></div>

  <svg class="brand-wave" viewBox="0 0 1200 555" aria-hidden="true">
    <defs>
      <linearGradient id="waveFill" x1="0" y1="0" x2="0" y2="1">
        <stop offset="0" stop-color="#6a2c9c"/>
        <stop offset="1" stop-color="#4a1f6c"/>
      </linearGradient>
      <linearGradient id="waveEdge" x1="0" y1="0" x2="1" y2="0">
        <stop offset="0" stop-color="#b07ad8"/>
        <stop offset="0.5" stop-color="#e2ccf5"/>
        <stop offset="1" stop-color="#a672d0"/>
      </linearGradient>
    </defs>
    <path d="M0,378 C90,352 210,342 330,354 C560,378 690,478 800,505 C950,540 1100,460 1200,388 L1200,555 L0,555 Z" fill="url(#waveFill)"/>
    <path d="M0,378 C90,352 210,342 330,354 C560,378 690,478 800,505 C950,540 1100,460 1200,388" fill="none" stroke="url(#waveEdge)" stroke-width="3" opacity="0.9"/>
    <path d="M0,390 C120,366 240,362 360,374 C580,398 700,494 820,518 C960,546 1110,472 1200,404" fill="none" stroke="var(--purple-glow)" stroke-width="1.5" opacity="0.45"/>
    <circle cx="215" cy="360" r="4" fill="#ffffff" opacity="0.8"/>
    <circle cx="975" cy="512" r="4" fill="#ffffff" opacity="0.8"/>
  </svg>

  <div class="ribbon">
    <svg viewBox="0 0 394 73" aria-hidden="true">
      <defs>
        <linearGradient id="ribbonFill" x1="0" y1="0" x2="0" y2="1">
          <stop offset="0" stop-color="#ffffff"/>
          <stop offset="1" stop-color="#dedede"/>
        </linearGradient>
      </defs>
      <path d="M0,0 H394 L380,36.5 L394,73 H0 Z" fill="url(#ribbonFill)"/>
    </svg>
    <span class="ribbon-label">Just Listed</span>
  </div>

  <div class="brand-name">
    <span class="brand-main">Ormond</span>
    <span class="brand-sub">Real Estate</span>
  </div>
</div>
</body>
</html>
```